Commercial / Truck Battery Label

We need a high definition label design to send to a commercial printer for a Commercial/Truck Battery Label
I will upload our current truck battery label for you to get an idea of what we are looking for. Along with some competitor images and other logos for the label that we have on file. If we need to purchase a few images to make the label we can do that but need to see the design first.
The Labels need to have a plain white area which is 60mm Long x 40mm High along the bottom left corner. We will use this area for the battery specifications.
The Top Six Warning Icons downloaded also need to be on the label, perhaps along the bottom to the right of the white area in pairs. The icons size can be between 10mm x 10mm and 20mm x 20mm
The dimensions of the label need to be 390mm Long and the height needs to be both 140mm and 180mm. Same label 2 different sizes.
I would like to keep the terms : "SUPER HEAVY DUTY" and "THE STEADY CHARGE THAT HOLDS" on the label somewhere. Maybe replacing the word batteries or commercial with SUPER HEAVY DUTY under the right side of the VOLTMASTRO Logo.
The labels will be used predominantly on Black batteries, so a colour scheme or design to suit that.
I don't mind a completely fresh design or a reworking of the old design.
Look and feel
Each slider illustrates characteristics of the customer's brand and the style your logo design should communicate.

```html
<!DOCTYPE html>
<html lang="en">
<head>
<meta charset="utf-8">
<title>VOLTMASTRO Batteries – Super Heavy Duty Label</title>
<link rel="stylesheet" href="https://fonts.googleapis.com/css2?family=Exo+2:ital,wght@0,800;0,900;1,800;1,900&display=swap">
<style>
  :root {
    --label-black: #1c1c1e;
    --label-black-deep: #111113;
    --brand-blue: #0b3a8f;
    --brand-blue-light: #2f6fd8;
    --brand-red: #e3061a;
    --paper-white: #ffffff;
    --icon-ink: #1c1c1e;
  }
  html, body {
    margin: 0;
    padding: 0;
    width: 1200px;
    height: 431px;
    overflow: hidden;
    background: #ffffff;
  }
  .battery-label {
    position: relative;
    width: 1200px;
    height: 431px;
    border-radius: 22px;
    overflow: hidden;
    background: radial-gradient(ellipse at 60% 40%, #2b2b2e 0%, var(--label-black) 55%, var(--label-black-deep) 100%);
    font-family: "Exo 2", "Arial Black", sans-serif;
  }
  .label-art {
    position: absolute;
    inset: 0;
    width: 1200px;
    height: 431px;
  }
  .brand-name text {
    font-family: "Exo 2", "Arial Black", sans-serif;
    font-style: normal;
    font-weight: 900;
    fill: var(--brand-red);
  }
  .range-title text {
    font-family: "Exo 2", "Arial Black", sans-serif;
    font-style: italic;
    font-weight: 900;
    paint-order: stroke fill;
    stroke-linejoin: round;
  }
  .partner-name {
    position: absolute;
    left: 1010px;
    top: 44px;
    width: 130px;
    text-align: center;
    color: var(--brand-blue-light);
    font-weight: 800;
    font-style: normal;
    font-size: 30px;
    letter-spacing: 0.5px;
    line-height: 1;
  }
  .spec-panel {
    position: absolute;
    left: 0;
    bottom: 0;
    width: 186px;
    height: 124px;
    background: var(--paper-white);
    border-top-right-radius: 18px;
  }
</style>
</head>
<body>
  <main class="battery-label">
    <svg class="label-art" viewBox="0 0 1200 431" xmlns="http://www.w3.org/2000/svg">
      <defs>
        <linearGradient id="heavyDutyFill" x1="0" y1="0" x2="0" y2="1">
          <stop offset="0" stop-color="#6fa2f2"/>
          <stop offset="0.5" stop-color="#1d4fb8"/>
          <stop offset="1" stop-color="#0a2a72"/>
        </linearGradient>
        <linearGradient id="taglineFill" x1="0" y1="0" x2="0" y2="1">
          <stop offset="0" stop-color="#ff5a64"/>
          <stop offset="0.5" stop-color="#d0061a"/>
          <stop offset="1" stop-color="#7a0410"/>
        </linearGradient>
      </defs>

      <!-- white swoosh band -->
      <path class="swoosh" fill="#ffffff"
            d="M0,52 C320,70 720,150 1200,232 L1200,262 C820,215 420,150 0,142 Z"/>

      <!-- brand name and product line -->
      <g class="brand-name">
        <text x="108" y="200" font-size="170"
              textLength="835" lengthAdjust="spacingAndGlyphs">VOLTMASTRO</text>
        <text x="560" y="268" font-size="52"
              textLength="340" lengthAdjust="spacingAndGlyphs">BATTERIES</text>
      </g>

      <!-- range title and tagline -->
      <g class="range-title">
        <text x="620" y="360" font-size="56" fill="url(#heavyDutyFill)" stroke="#ffffff" stroke-width="3"
              textLength="458" lengthAdjust="spacingAndGlyphs">SUPER HEAVY DUTY</text>
        <text x="736" y="396" font-size="31" fill="url(#taglineFill)" stroke="#ffffff" stroke-width="1.5"
              textLength="402" lengthAdjust="spacingAndGlyphs">THE STEADY CHARGE THAT HOLDS</text>
      </g>

      <!-- safety warning icons -->
      <g class="warning-icons" fill="#ffffff" stroke="#ffffff">
        <g class="icon-caution">
          <circle cx="247" cy="382" r="16" stroke="none"/>
          <rect x="244.5" y="371" width="5" height="14" rx="2" fill="var(--icon-ink)" stroke="none"/>
          <circle cx="247" cy="390" r="2.6" fill="var(--icon-ink)" stroke="none"/>
        </g>
        <g class="icon-eye-protection">
          <circle cx="291" cy="382" r="16" stroke="none"/>
          <rect x="280" y="377" width="9" height="7" rx="3" fill="var(--icon-ink)" stroke="none"/>
          <rect x="293" y="377" width="9" height="7" rx="3" fill="var(--icon-ink)" stroke="none"/>
          <rect x="288" y="379" width="6" height="2" fill="var(--icon-ink)" stroke="none"/>
        </g>
        <g class="icon-keep-away">
          <circle cx="336" cy="382" r="14.5" fill="none" stroke-width="3"/>
          <path d="M333,372 L339,376 L334,382 L340,388 L335,393" fill="none" stroke-width="2.4"/>
          <line x1="326" y1="372" x2="346" y2="392" stroke-width="3"/>
        </g>
        <g class="icon-corrosive">
          <path d="M382,367 L398,395 L366,395 Z" fill="none" stroke-width="3" stroke-linejoin="round"/>
          <rect x="375" y="386" width="14" height="4" stroke="none"/>
          <circle cx="382" cy="379" r="2.4" stroke="none"/>
        </g>
        <g class="icon-no-flame">
          <circle cx="428" cy="382" r="14.5" fill="none" stroke-width="3"/>
          <path d="M428,372 C433,378 434,384 428,390 C422,384 423,378 428,372 Z" stroke="none"/>
          <line x1="418" y1="372" x2="438" y2="392" stroke-width="3"/>
        </g>
        <g class="icon-explosive">
          <path d="M475,367 L491,395 L459,395 Z" fill="none" stroke-width="3" stroke-linejoin="round"/>
          <path d="M475,378 L477,384 L482,383 L478,387 L481,392 L475,389 L469,392 L472,387 L468,383 L473,384 Z" stroke="none"/>
        </g>
      </g>
    </svg>

    <div class="partner-name">KORVEN</div>
    <div class="spec-panel" aria-label="Battery specifications area"></div>
  </main>
</body>
</html>
```